A new website for Electrical Contractor Business

We are looking for a unique and new WordPress website design which would include 5 Pages - Home Page, Meet the Team, Our Services, Our Projects and Contact Us page.

The global theme for the website needs to be professional but simple to navigate as we cater for both business and home owner customers.

Our core business service is targeted around lighting from single room decorative to large office so the theme should incorporate this in some way.

The home page should include;
Our business logo, Contact number, Email address, small Image rotation box - Highlighting pervious projectsText box - With welcome message, chirpnet feed news reel/Customer feed back box.

I would also like to see a 2 boxes for the separate customer types we services. Business and Home Owner. each box will have a small image with a small text description with a link to the area of the services page relevant to that customer type.

Meet the team page -This will be introducing potential customers to the team so I would like it to include for each team member. Something like a small image and text area which will introduce an outline of the team members skills and abilities.

Our Services page This page will be outlining the different services on offer to the both customer types business and homeowner. Each service should have an image with text description of the service would good here.

Our projects page-Will include images of pervious projects and work we have completed along with a text area for the project description/ outliner.

Contact Us page - Should include a contact form which should include an option for the customer to quest us to call them back, also a selection box for them to inform us our how they found our details would be good.

Colour - The theme colours can be taken from the logo or feel free to impress with your own imagination.

Remember we are looking for a website that will interest our customers enough to except our services or be drawn further into the website.. So call to action links to other areas of the site/ contact page are welcome

Target Market(s)

Business - Office, warehousing and Large Store - lighting and Power
Home owner lighting and power

Coding

Coded - Design and coding required

Number of Pages Required

5+ page

Font styles to use
Serif
Sans Serif

Colors

Designer to choose colors to be used in the design.

Requirements
Must have
• Logo integrated into the website design - i.e. website colours which allow the logo to blend into the design.
Nice to have
• Custom but professional theme catering to business customers, but also show that we do provide services to home owners too.
Should not have
• Sorry am not interested in one oversized block image on rotation covering half the home page.. Images will be needed but not a single block over sized frame with not text, shape. Please use your imagination when considering this design

```html
<!DOCTYPE html>
<html lang="en">
<head>
<meta charset="utf-8">
<title>Brightline Electrical — Home</title>
<link rel="stylesheet" href="https://fonts.googleapis.com/css2?family=Barlow:wght@400;500;600&family=Raleway:wght@300;400;500&family=Montserrat:wght@600&family=Libre+Baskerville:wght@700&display=swap">
<style>
:root{
  --orange:#f26336;
  --navy:#1f2a54;
  --sky:#2b9fe2;
  --footer:#241f5e;
  --ink:#2b2b33;
  --muted:#8a8a92;
  --light:#f4f4f5;
  --line:#e4e4e7;
}
*{margin:0;padding:0;box-sizing:border-box}
html,body{width:1200px;height:3589px;overflow:hidden}
body{position:relative;background:#fff;font-family:"Barlow",sans-serif;color:var(--ink)}
h1,h2,h3,h4{font-weight:400}
.abs{position:absolute}
a{color:inherit;text-decoration:none}

/* top bar */
.topbar{left:0;top:0;width:1200px;height:33px;background:#ededed;font-size:12px}
.topbar .lang{left:59px;top:9px;letter-spacing:.5px;color:#333}
.topbar .lang::after{content:"";display:inline-block;margin-left:7px;border:4px solid transparent;border-top-color:#333;vertical-align:-2px}
.topbar .mail{left:822px;top:10px;color:#888;font-size:11px}
.topbar .hot{left:986px;top:9px;color:var(--orange);font-size:12px}
.topbar svg{vertical-align:-2px;margin-right:5px}

/* header */
.header{left:0;top:33px;width:1200px;height:81px;border-bottom:1px solid var(--line)}
.brand{left:90px;top:15px;display:flex;align-items:center;gap:10px}
.brand-mark{width:52px;height:52px;border-radius:50%;background:var(--navy)}
.brand-name{font-weight:500;font-size:21px;letter-spacing:1px;color:var(--navy)}
.divider{left:341px;top:20px;width:1px;height:46px;background:var(--line)}
.nav{left:374px;top:33px;display:flex;gap:33px;font-size:13px;font-weight:500;letter-spacing:.3px;color:#2c3360}
.nav .active{color:var(--orange)}
.socials{left:1023px;top:28px;display:flex;gap:6px}
.socials span{width:26px;height:26px;border:1.4px solid #555;border-radius:50%}

/* hero */
.hero{left:52px;top:137px;width:1096px;height:415px;background:radial-gradient(ellipse at 75% 35%,#5a3fe6 0%,#2a1c8a 35%,#120b3c 75%,#0a0824 100%)}
.hero-copy{left:160px;top:254px;color:#fff}
.hero-copy h1{font-weight:400;font-size:41px;line-height:44px;letter-spacing:.3px}
.hero-copy .hl{color:var(--sky)}
.hero-copy p{margin-top:6px;font-size:13px;letter-spacing:3.4px}
.btn{display:inline-block;text-align:center;font-size:12px;font-weight:500;letter-spacing:1px}
.btn-orange{left:163px;top:379px;width:146px;height:39px;line-height:39px;background:var(--orange);color:#fff}
.btn-white{left:316px;top:379px;width:147px;height:39px;line-height:39px;background:#fff;color:#222}

/* welcome */
.welcome-box{left:184px;top:609px;width:500px;height:346px;background:var(--light)}
.welcome-accent{left:172px;top:610px;width:12px;height:112px;background:#8c8c91}
.welcome-kicker{left:241px;top:658px;font-family:"Raleway",sans-serif;font-size:19px;color:#777}
.welcome-title{left:241px;top:681px;font-size:31px;font-weight:500;letter-spacing:.5px;color:#111}
.welcome-text{left:244px;top:722px;width:372px;font-family:"Raleway",sans-serif;font-weight:300;font-size:13px;line-height:23.6px;color:#888}
.btn-pill{left:248px;top:878px;width:144px;height:35px;line-height:35px;border-radius:18px;background:var(--orange);color:#fff;font-family:"Raleway",sans-serif;font-size:13.5px;text-align:center}

/* customer types */
.tile-label{width:142px;height:99px;background:var(--navy);color:#fff;padding:26px 0 0 29px;font-size:23px;font-weight:600;line-height:24px}
.tile-label svg{position:absolute;right:20px;top:34px}
.tile-divider{left:596px;top:1060px;width:10px;height:300px;background:var(--orange);transform:skewX(-12deg);border-left:3px solid #fff;border-right:3px solid #fff}

/* projects */
.section-title{left:0;width:1200px;text-align:center;font-size:26px;letter-spacing:.5px;color:var(--navy)}
.section-title .hl{color:var(--orange)}
.tabs{left:464px;top:1433px;width:265px;height:33px}
.gallery{left:0;top:1481px;width:1200px;height:600px;display:grid;grid-template-columns:repeat(4,300px);grid-template-rows:repeat(2,300px)}
.gallery>.tile{position:relative;overflow:hidden}
.caption{position:absolute;left:0;bottom:0;width:300px;height:108px;background:#fff;padding:20px 0 0 30px}
.caption h3{font-family:"Montserrat",sans-serif;font-weight:600;font-size:16px;color:#111}
.caption p{margin-top:10px;font-size:10px;line-height:21px;color:#333}
.plus{position:absolute;left:17px;top:18px;width:29px;height:29px;border-radius:50%;background:var(--orange);color:#fff;text-align:center;line-height:27px;font-size:20px}

/* testimonials */
.testi-bg{left:0;top:2081px;width:1200px;height:720px;background:linear-gradient(90deg,#e9ebf0 0%,#f7f7f9 35%,#fafafa 100%)}
.kicker{left:0;width:1200px;text-align:center;font-size:23px;letter-spacing:1px;color:var(--orange)}
.avatar{left:554px;top:2281px;width:92px;height:92px;border-radius:50%;background:linear-gradient(#e6e6e6,#9a9aa0);border:3px solid #fff}
.testi-card{left:284px;top:2336px;width:633px;height:265px;background:#fff;box-shadow:0 2px 10px rgba(0,0,0,.06);text-align:center}
.testi-card blockquote{margin-top:80px;font-size:21px;line-height:32px;color:#444}
.testi-card .name{margin-top:24px;font-size:21px;color:var(--orange)}
.testi-card .org{margin-top:4px;font-size:13px;color:#888;letter-spacing:.5px}
.arrow{width:42px;height:42px;border-radius:50%;background:#f7b9a6}

/* signup */
.signup-band{left:0;top:2801px;width:1200px;height:296px;background:#f3f3f5}
.signup-title{left:0;top:2852px;width:1200px;text-align:center;font-family:"Libre Baskerville",serif;font-weight:700;font-size:27px;color:#2a2d3e;letter-spacing:.5px}
.signup-note{left:0;top:2911px;width:1200px;text-align:center;font-family:"Libre Baskerville",serif;font-size:11px;color:#555}
.field{left:326px;top:2952px;width:410px;height:39px;background:#fff;border:1px solid #ddd;font-size:11px;color:#777;padding:12px 10px}
.subscribe{left:736px;top:2952px;width:138px;height:39px;background:var(--navy);color:#fff;text-align:center;line-height:39px;font-weight:600;font-size:14px;letter-spacing:.5px}
.dots{left:479px;top:3033px;display:flex;gap:13px}
.dots span{width:19px;height:19px;border-radius:50%}

/* footer */
.footer{left:0;top:3097px;width:1200px;height:492px;background:var(--footer);color:#fff}
.fcol h4{font-size:21px;font-weight:500;letter-spacing:.3px}
.ftext{font-family:"Raleway",sans-serif;font-size:12px;line-height:25px;color:#b8b6d6}
.femail{width:212px;height:35px;background:#2d2870;border-radius:3px;font-family:"Raleway",sans-serif;font-size:10.5px;color:#9c99c8;padding:11px 12px}
.tweet{display:flex;gap:16px;font-family:"Raleway",sans-serif;font-size:11px;line-height:15px;color:#b8b6d6}
.tweet i{flex:none;width:13px;height:13px;border-radius:50%;background:var(--sky);margin-top:3px}
.thumbs{display:grid;grid-template-columns:repeat(3,57px);gap:12px 8px}
.thumbs span{width:57px;height:57px}
.fsoc{display:flex;gap:14px}
.fsoc span{width:13px;height:13px;border-radius:50%;background:#8f8cbd}
.fbar{left:122px;top:3505px;width:1058px;height:1px;background:#3a3578}
.copy{left:122px;top:3522px;font-family:"Raleway",sans-serif;font-size:11.5px;color:#b8b6d6}
.fnav{left:751px;top:3519px;display:flex;gap:16px;font-size:12px;font-weight:500;color:#fff}
.fnav .active{color:var(--orange)}
.totop{left:1143px;top:3492px;width:36px;height:36px;border:1.5px solid var(--orange);border-radius:5px}
</style>
</head>
<body>

<!-- top bar -->
<div class="abs topbar">
  <span class="abs lang">ENGLISH</span>
  <span class="abs mail"><svg width="12" height="9" viewBox="0 0 12 9"><rect x=".5" y=".5" width="11" height="8" fill="#999"/><path d="M.5 .5 6 5l5.5-4.5" stroke="#ededed" fill="none"/></svg>info@brightline.example</span>
  <span class="abs hot"><svg width="13" height="13" viewBox="0 0 24 24"><path d="M6.6 10.8a15 15 0 0 0 6.6 6.6l2.2-2.2a1 1 0 0 1 1-.25 11.4 11.4 0 0 0 3.6.57 1 1 0 0 1 1 1V20a1 1 0 0 1-1 1A17 17 0 0 1 3 4a1 1 0 0 1 1-1h3.5a1 1 0 0 1 1 1c0 1.25.2 2.45.57 3.57a1 1 0 0 1-.25 1z" fill="#333"/></svg>HOTLINE : 01234-567-890</span>
</div>

<!-- header -->
<header class="abs header">
  <div class="abs brand"><span class="brand-mark"></span><span class="brand-name">BRIGHTLINE</span></div>
  <span class="abs divider"></span>
  <nav class="abs nav">
    <a class="active">HOME</a><a>MEET THE TEAM</a><a>OUR SERVICES</a><a>PROJECTS</a><a>CONTACT US</a>
  </nav>
  <div class="abs socials"><span></span><span></span><span></span><span></span></div>
</header>

<!-- hero -->
<section>
  <div class="abs hero" role="img" aria-label="Large venue lit with blue and purple LED stage lighting"></div>
  <div class="abs hero-copy">
    <h1>LIGHTING AND POWER SOLUTIONS<br><span class="hl">HOME</span> AND <span class="hl">CORPORATE</span> SPACES</h1>
    <p>GET STARTED ON YOUR NEXT PROJECT WITH OUR TEAM.</p>
  </div>
  <a class="abs btn btn-orange">LEARN MORE</a>
  <a class="abs btn btn-white">CONTACT US</a>
</section>

<!-- welcome -->
<section>
  <div class="abs welcome-box"></div>
  <div class="abs welcome-accent"></div>
  <svg class="abs" style="left:636px;top:604px" width="436" height="350" viewBox="0 0 436 350" role="img" aria-label="Warm pendant lights glowing over a dining table">
    <defs><radialGradient id="wimg" cx=".55" cy=".35" r=".8"><stop offset="0" stop-color="#f5c46a"/><stop offset=".35" stop-color="#8a5a2c"/><stop offset="1" stop-color="#2e1d12"/></radialGradient></defs>
    <polygon points="46,17 422,2 434,348 2,336" fill="url(#wimg)"/>
  </svg>
  <div class="abs welcome-kicker">Welcome</div>
  <h2 class="abs welcome-title">WHO WE ARE?</h2>
  <p class="abs welcome-text">Brightline Electrical is a local team of licensed electricians who take pride in safe, tidy work. From a single decorative pendant to full office and warehouse fit-outs, we design and install lighting and power for homes and businesses. Our work can be found in homes, offices, shops and large stores across the region.</p>
  <a class="abs btn-pill">Learn More</a>
</section>

<!-- customer types -->
<section>
  <svg class="abs" style="left:0;top:955px" width="1200" height="205" viewBox="0 0 1200 205">
    <path d="M0 90 C40 80 90 98 130 70 C160 45 190 60 220 30 C260 10 320 40 380 22 C460 2 520 30 600 20 C680 8 760 30 840 14 C920 2 980 40 1040 30 C1090 24 1120 60 1160 70 L1200 78 L1200 205 L0 205 Z" fill="#f2f2f3"/>
  </svg>
  <div class="abs" style="left:231px;top:1066px;width:369px;height:266px;background:radial-gradient(ellipse at 40% 20%,#fff3d6 0%,#e2cfa6 35%,#9a8258 75%,#5e4a30)" role="img" aria-label="Home kitchen with warm downlights and pendant lamps"></div>
  <div class="abs" style="left:600px;top:1063px;width:431px;height:269px;background:linear-gradient(180deg,#eef3f8 0%,#c7d3df 35%,#7d8ea3 75%,#4a5668)" role="img" aria-label="Open-plan office lit by ceiling LED panels"></div>
  <a class="abs tile-label" style="left:231px;top:1233px">HOME<br>OWNER<svg width="18" height="34" viewBox="0 0 18 34"><polygon points="0,0 18,17 0,34" fill="#fff"/></svg></a>
  <a class="abs tile-label" style="left:631px;top:1233px;width:162px">OFFICE<br>STORE<svg width="18" height="34" viewBox="0 0 18 34"><polygon points="0,0 18,17 0,34" fill="#fff"/></svg></a>
  <div class="abs tile-divider"></div>
</section>

<!-- projects -->
<section>
  <h2 class="abs section-title" style="top:1387px">OUR <span class="hl">PROJECTS</span></h2>
  <svg class="abs tabs" viewBox="0 0 265 33" width="265" height="33">
    <rect width="265" height="33" fill="var(--navy)"/>
    <polygon points="0,0 130,0 114,33 0,33" fill="#b9bccd"/>
    <text x="72" y="21" text-anchor="middle" font-family="Barlow, sans-serif" font-size="13" fill="#2c3360">Home</text>
    <text x="200" y="21" text-anchor="middle" font-family="Barlow, sans-serif" font-size="13" fill="#fff">Corporate</text>
  </svg>
  <div class="abs gallery">
    <div class="tile" style="background:linear-gradient(135deg,#8d8a86,#d8d2c8 55%,#eee9e0)" role="img" aria-label="Living room lit by a round pendant lamp"></div>
    <div class="tile" style="background:linear-gradient(180deg,#b8b5b0,#d9d6d1)" role="img" aria-label="Bathroom with recessed shower lighting">
      <span class="plus">+</span>
      <div class="caption"><h3>Newest project for Nordhem</h3><p>Complete LED upgrade across showroom and storage<br>areas, cutting energy use while improving visibility...</p></div>
    </div>
    <div class="tile" style="background:linear-gradient(180deg,#d6d6d6,#eaeaea)" role="img" aria-label="Showroom chair under spot lighting"></div>
    <div class="tile" style="background:linear-gradient(180deg,#8e8e8e,#b5b0a8 70%,#7b6f60)" role="img" aria-label="Reception seating with wall lighting"></div>
    <div class="tile" style="background:linear-gradient(135deg,#b9b7b2,#e7e4de 60%,#f2efe9)" role="img" aria-label="Bright lounge with floor lamp"></div>
    <div class="tile" style="background:linear-gradient(180deg,#7f6b58,#a99a8a 55%,#e0ddd8)" role="img" aria-label="Bedroom with geometric pendant light"></div>
    <div class="tile" style="background:linear-gradient(90deg,#8a6a4c,#b5a999 45%,#d0d6d8)" role="img" aria-label="Spa bathroom with under-floor lighting"></div>
    <div class="tile" style="background:linear-gradient(135deg,#eeeeee,#d9d4cc 60%,#b08a5e)" role="img" aria-label="Bedroom with wire pendant and reading lamp"></div>
  </div>
</section>

<!-- testimonials -->
<section>
  <div class="abs testi-bg" role="img" aria-label="Faint wiring plan backdrop"></div>
  <div class="abs kicker" style="top:2185px">TESTIMONIALS</div>
  <h2 class="abs section-title" style="top:2224px;font-size:29px">OUR CUSTOMERS SAY</h2>
  <div class="abs testi-card">
    <blockquote>Fast, tidy and friendly – our new office lighting is brighter,<br>cheaper to run and was fitted without any downtime.</blockquote>
    <div class="name">Laura Bennett</div>
    <div class="org">Marketing Meadow Studio Pty Ltd.</div>
  </div>
  <div class="abs avatar" role="img" aria-label="Customer portrait"></div>
  <svg class="abs arrow" style="left:160px;top:2447px" viewBox="0 0 42 42"><path d="M24 13 16 21l8 8" stroke="#fff" stroke-width="2" fill="none"/></svg>
  <svg class="abs arrow" style="left:1015px;top:2447px" viewBox="0 0 42 42"><path d="M18 13l8 8-8 8" stroke="#fff" stroke-width="2" fill="none"/></svg>
</section>

<!-- signup -->
<section>
  <div class="abs signup-band"></div>
  <h2 class="abs signup-title">SIGN UP FOR OUR DISCOUNTS TODAY!</h2>
  <p class="abs signup-note">You may unsubscribe at any moment. For that purpose, please find our contact info in the legal notice.</p>
  <div class="abs field">Your email address</div>
  <a class="abs subscribe">Subscribe</a>
  <div class="abs dots">
    <span style="background:#3b5998"></span><span style="background:#1da1f2"></span><span style="background:#f39c12"></span><span style="background:#e74c3c"></span><span style="background:#dd4b39"></span><span style="background:#cb2027"></span><span style="background:#111"></span><span style="background:#c13584"></span>
  </div>
</section>

<!-- footer -->
<footer class="abs footer">
  <div class="abs fcol" style="left:131px;top:80px">
    <h4>About Us</h4>
    <p class="ftext" style="margin-top:20px;width:210px">Licensed electricians for homes and business. Lighting, power and safe wiring, done right the first time.</p>
    <div class="femail" style="margin-top:26px">Email Address</div>
  </div>
  <div class="abs fcol" style="left:373px;top:80px;width:200px">
    <h4>Chirpnet Feed</h4>
    <div class="tweet" style="margin-top:30px"><i></i><p>New warehouse LED fit-out finished this week, ahead of schedule.<br>https://chp.link/4kQw82</p></div>
    <div class="tweet" style="margin-top:24px"><i></i><p>Thinking of new kitchen lighting? Book a free home quote today.<br>https://chp.link/4kQw82</p></div>
  </div>
  <div class="abs fcol" style="left:611px;top:80px">
    <h4>Snapgrid</h4>
    <div class="thumbs" style="margin-top:30px">
      <span style="background:#8a6a50" role="img" aria-label="Kitchen lighting photo"></span>
      <span style="background:#3d6aa0" role="img" aria-label="Office lighting photo"></span>
      <span style="background:#6a3a30" role="img" aria-label="Venue lighting photo"></span>
      <span style="background:#b08070" role="img" aria-label="Pendant lamp photo"></span>
      <span style="background:#7f94b0" role="img" aria-label="Store lighting photo"></span>
      <span style="background:#4a4e6a" role="img" aria-label="Warehouse lighting photo"></span>
    </div>
  </div>
  <div class="abs fcol" style="left:853px;top:80px;width:220px">
    <h4>Contact Us</h4>
    <p class="ftext" style="margin-top:26px;line-height:18px;font-size:11.5px">Address: 12 Harbour Lane, Riverton, Australia</p>
    <p class="ftext" style="margin-top:24px;line-height:18px;font-size:11.5px">Phone: 8 800 555.010.22 Email:<br><span style="color:#fff">info@brightline.example</span></p>
    <div class="fsoc" style="margin-top:28px"><span></span><span></span><span></span><span></span></div>
  </div>
</footer>
<div class="abs fbar"></div>
<div class="abs copy">© 2018 Brightline Electrical– Lighting and power services</div>
<nav class="abs fnav"><a class="active">Home</a><a>Meet the team</a><a>Our services</a><a>Projects</a><a>Contact us</a></nav>
<svg class="abs totop" viewBox="0 0 36 36"><path d="M13 20l5-5 5 5" stroke="var(--orange)" stroke-width="2" fill="none"/></svg>

</body>
</html>
```